Trifold Brochure

This is relatively easy. We already have a trifold made we simply want to update the LOOK to look more like our current website. All content would stay the same the only thing that would change would be the fonts, colors and background images to match the current website.

I have attached a word doc of the old trifold brochure. We would want the content to remain on the same pages of the trifold. Again all you are doing is updating the font, logo, colors and any background images. Please comment with any questions.

This is a 5 day project!

Requirements
Must have
• Logo, colors and fonts to match our current website.
http://www.brambleworksgroup.example/

```html
<!DOCTYPE html>
<html lang="en">
<head>
<meta charset="utf-8">
<title>Brambleworks Group – Rack Brochure Cover</title>
<link href="https://fonts.googleapis.com/css2?family=Arimo:wght@400;700&display=swap" rel="stylesheet">
<style>
  :root {
    --stage: #a3a3a3;
    --paper: #e2ecd2;
    --paper-light: #edf3e2;
    --leaf: #7a9660;
    --leaf-dark: #6a8651;
    --ink: #1f2418;
    --white: #ffffff;
  }
  * { box-sizing: border-box; margin: 0; padding: 0; }
  html, body {
    width: 1200px;
    height: 800px;
    overflow: hidden;
  }
  body {
    background: var(--stage);
    font-family: "Arimo", Arial, sans-serif;
    display: flex;
    align-items: center;
    justify-content: center;
  }
  .brochure-cover {
    width: 350px;
    height: 750px;
    background: linear-gradient(180deg, var(--paper-light), var(--paper));
    display: flex;
    flex-direction: column;
  }
  .edge-band {
    height: 18px;
    background: var(--leaf);
    flex: none;
  }
  .brand-block {
    height: 190px;
    display: flex;
    flex-direction: column;
    align-items: center;
    justify-content: center;
    gap: 22px;
  }
  .brand-mark {
    display: flex;
    align-items: center;
    gap: 12px;
    color: var(--leaf-dark);
    font-weight: 700;
    font-size: 34px;
    letter-spacing: 0.5px;
  }
  .brand-mark .dot {
    width: 22px;
    height: 22px;
    border-radius: 50%;
    background: var(--leaf);
  }
  .company-name {
    font-size: 17px;
    color: var(--ink);
  }
  .headline-band {
    height: 90px;
    background: var(--leaf);
    color: var(--paper-light);
    display: flex;
    align-items: center;
    justify-content: center;
    text-align: center;
  }
  .headline-band h1 {
    font-size: 28px;
    line-height: 1.15;
    font-weight: 700;
  }
  .hero-photo {
    height: 290px;
    background: linear-gradient(180deg, #6f6f86 0%, #a9879a 35%, #c99a8e 50%, #8e7f8a 70%, #8a8090 100%);
  }
  .mission {
    flex: 1;
    display: flex;
    align-items: center;
    justify-content: center;
    text-align: center;
    padding: 0 30px;
  }
  .mission p {
    color: var(--leaf);
    font-weight: 700;
    font-size: 19px;
    line-height: 1.2;
  }
</style>
</head>
<body>
  <article class="brochure-cover">
    <div class="edge-band"></div>
    <header class="brand-block">
      <div class="brand-mark"><span class="dot"></span>Brambleworks</div>
      <p class="company-name">Brambleworks Group, LLC</p>
    </header>
    <div class="headline-band">
      <h1>Rebuild Safer<br>Stronger Better</h1>
    </div>
    <div class="hero-photo" role="img" aria-label="Photo of a parent and small child reaching hands toward each other on a beach at sunset, with a boat on the water"></div>
    <section class="mission">
      <p>We provide piling repair systems to allow for cost effective reconstruction and modifications to structures on pilings</p>
    </section>
    <div class="edge-band"></div>
  </article>
</body>
</html>
```